Kestrel Signs Facebook Banner Design

Design a facebook banner for a sign company. I would like to have a modern approach to it.

Product Offering:
Signs
Banners
Decals
Commercial Wraps

```html
<!DOCTYPE html>
<html lang="en">
<head>
<meta charset="utf-8">
<title>Kestrel Signs – Facebook Banner</title>
<link rel="stylesheet" href="https://fonts.googleapis.com/css2?family=Montserrat:wght@500;700;800&display=swap">
<style>
  :root {
    --page-bg: #e9eaea;
    --white: #ffffff;
    --ink: #3d3d40;
    --red-deep: #8c1117;
    --red: #c81f26;
    --button: #4a4a4d;
    --photo-grey: #b9bcbd;
  }
  * { margin: 0; padding: 0; box-sizing: border-box; }
  html, body {
    width: 1200px;
    height: 673px;
    overflow: hidden;
    background: var(--page-bg);
    font-family: "Montserrat", sans-serif;
  }
  .banner {
    position: absolute;
    left: 30px;
    top: 125px;
    width: 1140px;
    height: 422px;
    background: var(--white);
    overflow: hidden;
  }
  .banner-art {
    position: absolute;
    inset: 0;
    width: 100%;
    height: 100%;
  }
  .brand-name {
    position: absolute;
    left: 42px;
    top: 32px;
    font-weight: 800;
    font-size: 44px;
    line-height: 46px;
    letter-spacing: 1px;
    text-transform: uppercase;
    color: var(--ink);
  }
  .brand-name .second-line { display: block; padding-left: 86px; }
  .offering {
    position: absolute;
    left: 75px;
    top: 164px;
    color: var(--white);
  }
  .offering-title {
    font-weight: 800;
    font-size: 31px;
    line-height: 40px;
    margin-bottom: 8px;
  }
  .offering-list {
    list-style: none;
    font-weight: 800;
    font-size: 16px;
    line-height: 19px;
  }
  .offering-list li {
    position: relative;
    padding-left: 24px;
  }
  .offering-list li::before {
    content: "";
    position: absolute;
    left: 3px;
    top: 8px;
    width: 5px;
    height: 5px;
    border-radius: 50%;
    background: var(--white);
  }
  .contact {
    position: absolute;
    left: 128px;
    top: 356px;
    display: flex;
    align-items: center;
    gap: 9px;
  }
  .contact-icon {
    width: 49px;
    height: 49px;
    border-radius: 50%;
    background: radial-gradient(circle at 45% 40%, var(--red), var(--red-deep));
    display: flex;
    align-items: center;
    justify-content: center;
  }
  .contact-text {
    font-weight: 500;
    font-size: 14.5px;
    line-height: 18px;
    color: var(--ink);
  }
  .details-button {
    position: absolute;
    left: 366px;
    top: 363px;
    width: 214px;
    height: 35px;
    border-radius: 18px;
    background: var(--button);
    color: var(--white);
    font-weight: 800;
    font-size: 17px;
    line-height: 35px;
    text-align: center;
  }
</style>
</head>
<body>
  <section class="banner">
    <svg class="banner-art" viewBox="0 0 1140 422" xmlns="http://www.w3.org/2000/svg">
      <defs>
        <linearGradient id="redBand" x1="0" y1="0" x2="0" y2="1">
          <stop offset="0" stop-color="#8c1117"/>
          <stop offset="0.5" stop-color="#c81f26"/>
          <stop offset="1" stop-color="#8c1117"/>
        </linearGradient>
        <linearGradient id="streetPhoto" x1="0" y1="0" x2="1" y2="1">
          <stop offset="0" stop-color="#dcdedf"/>
          <stop offset="0.45" stop-color="#c4a79a"/>
          <stop offset="1" stop-color="#8f9192"/>
        </linearGradient>
        <linearGradient id="standsPhoto" x1="0" y1="0" x2="1" y2="1">
          <stop offset="0" stop-color="#5d9b4f"/>
          <stop offset="1" stop-color="#27313b"/>
        </linearGradient>
        <linearGradient id="carPhoto" x1="0" y1="0" x2="1" y2="1">
          <stop offset="0" stop-color="#eceeef"/>
          <stop offset="1" stop-color="#9a9ea1"/>
        </linearGradient>
        <linearGradient id="stopPhoto" x1="0" y1="0" x2="1" y2="1">
          <stop offset="0" stop-color="#a9adaf"/>
          <stop offset="0.5" stop-color="#b8262d"/>
          <stop offset="1" stop-color="#8a8d8f"/>
        </linearGradient>
        <linearGradient id="vansPhoto" x1="0" y1="0" x2="1" y2="1">
          <stop offset="0" stop-color="#f1f2f3"/>
          <stop offset="0.55" stop-color="#e4763a"/>
          <stop offset="1" stop-color="#6f7376"/>
        </linearGradient>
      </defs>

      <g role="img" aria-label="Blurred street scene behind the product photos">
        <polygon points="397,0 1140,0 1140,422 752,422" fill="url(#streetPhoto)"/>
      </g>
      <polygon class="corner-wedge" points="397,0 470,0 493,103" fill="#6a6c6e" opacity="0.55"/>

      <polygon class="red-band" points="0,126 505,126 685,342 0,342" fill="url(#redBand)"/>

      <g role="img" aria-label="Photo of printed roll-up banner stands">
        <rect x="564" y="39" width="190" height="190" rx="34" transform="rotate(45 659 134)" fill="url(#standsPhoto)" stroke="#ffffff" stroke-width="9"/>
      </g>
      <g role="img" aria-label="Photo of a stop sign">
        <rect x="867" y="65" width="190" height="190" rx="34" transform="rotate(45 962 160)" fill="url(#stopPhoto)" stroke="#ffffff" stroke-width="9"/>
      </g>
      <g role="img" aria-label="Photo of a white car with a tribal vinyl decal">
        <rect x="705" y="175" width="190" height="190" rx="34" transform="rotate(45 800 270)" fill="url(#carPhoto)" stroke="#ffffff" stroke-width="9"/>
      </g>
      <g role="img" aria-label="Photo of service vans with commercial wraps">
        <rect x="1008" y="194" width="190" height="190" rx="34" transform="rotate(45 1103 289)" fill="url(#vansPhoto)" stroke="#ffffff" stroke-width="9"/>
      </g>
    </svg>

    <h1 class="brand-name">Kestrel<span class="second-line">Signs</span></h1>

    <div class="offering">
      <h2 class="offering-title">Product Offering:</h2>
      <ul class="offering-list">
        <li>Signs</li>
        <li>Banners</li>
        <li>Decals</li>
        <li>Commercial Wraps</li>
      </ul>
    </div>

    <div class="contact">
      <div class="contact-icon">
        <svg width="26" height="22" viewBox="0 0 26 22" aria-hidden="true">
          <path d="M1 7 C1 2 25 2 25 7 L25 9 L19 9 L19 6 L7 6 L7 9 L1 9 Z" fill="#ffffff"/>
          <path d="M6 10 L20 10 L23 20 L3 20 Z" fill="#ffffff"/>
          <circle cx="13" cy="15" r="3.2" fill="#c81f26"/>
          <circle cx="13" cy="15" r="1.4" fill="#ffffff"/>
        </svg>
      </div>
      <p class="contact-text">Call for more info<br>+000 000 0000 00</p>
    </div>

    <div class="details-button">For more Details</div>
  </section>
</body>
</html>
```